Business Card Design

We are looking for a business card designed for our landscaping company. We do landscaping installation & Maintenance Services. We would like to see designs that have basic landscaping in background. We also think it is important to have both of our names and phone numbers on the card. We need something that stands out a little whether it is shape of the card or thickness or design.

Industry/Entity Type

Business

Contact Information for Business Card

Pale Ridge Yardworks, paleridgeyardworks@mailbrook.net, Dale Purvine 555-213-7690, Martin Kolbey 555-864-1037

```html
<!DOCTYPE html>
<html lang="en">
<head>
<meta charset="utf-8">
<title>Pale Ridge Yardworks – Business Card</title>
<link rel="stylesheet" href="https://fonts.googleapis.com/css2?family=Bodoni+Moda:wght@500;600&family=Open+Sans:wght@400&display=swap">
<style>
  :root {
    --backdrop: #e9e6df;
    --card-light: #bfe274;
    --card-mid: #a8d63e;
    --card-deep: #93c824;
    --ink: #1c1f14;
    --grass-dark: rgba(58, 96, 14, 0.42);
    --grass-mid: rgba(72, 112, 20, 0.24);
    --grass-fade: rgba(72, 112, 20, 0);
  }
  * { margin: 0; padding: 0; box-sizing: border-box; }
  html, body {
    width: 1200px;
    height: 892px;
    overflow: hidden;
    background: var(--backdrop);
  }
  .stage {
    width: 1200px;
    height: 892px;
    display: flex;
    align-items: center;
    justify-content: center;
  }
  .business-card {
    position: relative;
    width: 840px;
    height: 480px;
    background: linear-gradient(165deg, var(--card-light) 0%, var(--card-mid) 55%, var(--card-deep) 100%);
    box-shadow: 0 8px 24px rgba(0,0,0,0.18);
    overflow: hidden;
    color: var(--ink);
  }
  .grass-backdrop {
    position: absolute;
    left: 32%;
    right: 0;
    bottom: 0;
    height: 62%;
    background:
      radial-gradient(ellipse 55% 70% at 45% 100%, var(--grass-dark) 0%, var(--grass-mid) 45%, var(--grass-fade) 100%),
      radial-gradient(ellipse 45% 60% at 85% 70%, var(--grass-mid) 0%, var(--grass-fade) 100%),
      linear-gradient(to top, var(--grass-mid) 0%, var(--grass-fade) 70%);
  }
  .company-name {
    position: absolute;
    left: 80px;
    top: 52px;
    font-family: "Bodoni Moda", serif;
    font-weight: 600;
    font-size: 52px;
    letter-spacing: 0.5px;
    white-space: nowrap;
  }
  .title-rule {
    position: absolute;
    left: 60px;
    right: 40px;
    top: 128px;
    height: 2px;
    background: var(--ink);
  }
  .contact {
    position: absolute;
    top: 190px;
  }
  .contact--first { left: 62px; }
  .contact--second { left: 470px; top: 205px; }
  .contact-name {
    font-family: "Bodoni Moda", serif;
    font-weight: 500;
    font-size: 36px;
    line-height: 1.1;
  }
  .contact-phone {
    display: flex;
    align-items: center;
    gap: 12px;
    margin-top: 8px;
    font-family: "Open Sans", sans-serif;
    font-size: 27px;
  }
  .phone-icon { width: 20px; height: 20px; flex: none; }
  .email {
    position: absolute;
    left: 0;
    right: 0;
    top: 376px;
    text-align: center;
    padding-right: 40px;
    font-family: "Open Sans", sans-serif;
    font-size: 27px;
  }
</style>
</head>
<body>
<main class="stage">
  <article class="business-card">
    <div class="grass-backdrop" role="img" aria-label="Faint tall grass blades rising from the lower edge, landscaping background illustration"></div>
    <h1 class="company-name">Pale Ridge Yardworks</h1>
    <div class="title-rule"></div>

    <section class="contact contact--first">
      <p class="contact-name">Dale Purvine</p>
      <p class="contact-phone">
        <svg class="phone-icon" viewBox="0 0 20 20" aria-hidden="true">
          <rect width="20" height="20" fill="#1c1f14"/>
          <path d="M6 4 L9 4 L9.5 7 L8 8.2 C8.8 10 10 11.3 11.8 12 L13 10.5 L16 11 L16 14 C10 14.5 5.5 10 6 4 Z" fill="#bfe274"/>
        </svg>
        555-213-7690
      </p>
    </section>

    <section class="contact contact--second">
      <p class="contact-name">Martin Kolbey</p>
      <p class="contact-phone">
        <svg class="phone-icon" viewBox="0 0 20 20" aria-hidden="true">
          <rect width="20" height="20" fill="#1c1f14"/>
          <path d="M6 4 L9 4 L9.5 7 L8 8.2 C8.8 10 10 11.3 11.8 12 L13 10.5 L16 11 L16 14 C10 14.5 5.5 10 6 4 Z" fill="#a8d63e"/>
        </svg>
        555-864-1037
      </p>
    </section>

    <p class="email">paleridgeyardworks@mailbrook.net</p>
  </article>
</main>
</body>
</html>
```